Home Page for a Swiss based start up company, trading Natural & Health food ingredients (B2B)

I would like to create a home page for my new start up company (Velbrook Trade AG), the main field of activity is the trading and marketing of Natural and Health food ingredients towards the functional Food and Food supplements industry. (B2B).
Target Market : Functional Food and Food Supplement Manufacturers (B2B) based in Switzerland and Europe
The values I would like to convey are :
- sourcing of natural and health ingredients, (example : natural plant extracts, Omega 3, plant proteins, natural vitamins, vegan food ingredients...etc)
- Health & Nutritional Health
- Eco-friendly and Sustainability
- High Quality Standard in term of products and logistic services
- Trust and reliability
- Flexibility & speed to market
-Technical advice for the development of new products

The site will be translated in 3 languages (German, French, English)
Number of web pages : 5 : Home, About us, Products, Our Services, Contact

See here below attached Logo file.

Here some link of websites which can be taken as benchmark or source of inspiration
- https://quorvindel.com
- https://www.brimtaless.com/

Target Market(s)

Manufacturers of Functional Foods and Food Supplements in Switzerland and Europe (B2B)

Industry/Entity Type

B2B Trading of Natural & Health Ingredients

Font styles to use
Sans Serif

Colors
0054AA
0677BA
7BADD7
CADEEF
E8F1F8
0094D4
00A9DD
6FCCEA
C7EBF8
E9F6FB
00AB8E
00BBA5
67D7C9
C6EFE9
E9F9F6
59FF00
82FF00
B8FF75
E3FFCB
F4FFEA
FFF300
FFF600
FEFA6F
FFFEC7
FFFEE8
FFC000
F8CF3A
FAE287
FDF2CF
FEFAEE
F0912C
F2A743
F7CA91
FBE8D2
FDF5EE
EE7325
F08F49
F5BC92
FAE3D3
FDF4ED

Requirements
Must have
• inspiration towards nature, sustainability, vegan food, functional food & beverages, food supplements, nutritional health, low carbon footprint
Should not have
• animals, chemistry, food additives

```html
<!DOCTYPE html>
<html lang="en">
<head>
<meta charset="utf-8">
<title>Velbrook Trade AG – Home</title>
<link href="https://fonts.googleapis.com/css2?family=Playfair+Display:wght@400;500&family=Roboto:wght@400;500;700&family=Montserrat:wght@500&display=swap" rel="stylesheet">
<style>
:root{
  --green:#3b6533;
  --green-dark:#2f5429;
  --green-band:#44703a;
  --ink:#1d1d1d;
  --body:#333;
  --muted:#666;
  --footer:#141414;
  --white:#fff;
  --line:#d9d9d9;
}
*{margin:0;padding:0;box-sizing:border-box}
html,body{width:1200px;height:4402px;overflow:hidden;background:var(--white)}
body{position:relative;font-family:'Roboto',sans-serif;color:var(--body)}
.abs{position:absolute}
.serif{font-family:'Playfair Display',serif;font-weight:400}

/* header */
.brand{left:110px;top:10px;color:var(--green);text-align:center;line-height:0.95}
.brand .l1{font-size:40px;display:block}
.brand .l2{font-size:40px;display:block}
.search{left:666px;top:9px;width:350px;height:34px;border:1px solid #ccc;border-radius:17px;font-size:12px;color:#666;padding:9px 16px}
.search .btn{position:absolute;right:3px;top:2px;width:28px;height:28px;border-radius:50%;background:var(--green)}
.lang{left:1032px;top:9px;width:34px;height:34px;border-radius:50%;background:linear-gradient(180deg,#1d3f8f 0 45%,#c8202b 45% 60%,#fff 60% 70%,#c8202b 70%)}
.caret{left:1076px;top:22px;border:6px solid transparent;border-top-color:#222}
.nav{left:367px;top:51px;width:833px;height:48px;background:var(--green);clip-path:polygon(16px 0,100% 0,100% 100%,0 100%)}
.nav ul{list-style:none;display:flex;align-items:center;height:100%;padding-left:36px;gap:0}
.nav li{color:var(--white);font-weight:700;font-size:15px;letter-spacing:.2px}
.nav li.sep{margin:0 32px;font-weight:400}

/* hero */
.hero{left:0;top:99px;width:1200px;height:622px;background:linear-gradient(90deg,#8a5a22 0%,#b07a38 30%,#9c7a52 55%,#4a4438 80%,#2c2a26 100%)}
.hero h1{left:113px;top:210px;color:var(--white);font-size:66px}
.hero p{left:113px;top:290px;color:var(--white);font-family:'Montserrat',sans-serif;font-size:19px;line-height:34px;width:420px}
.hero .cta{left:113px;top:385px;width:188px;height:46px;border-radius:23px;background:var(--green);color:var(--white);font-weight:700;font-size:15px;display:flex;align-items:center;justify-content:center;gap:6px}
.dots{left:578px;top:578px;display:flex;gap:8px}
.dots i{width:10px;height:10px;border-radius:50%;background:rgba(255,255,255,.5)}
.dots i.on{background:var(--white)}

/* welcome */
.section-title{width:1200px;left:0;text-align:center;font-size:40px;color:var(--ink)}
.welcome-text{left:140px;top:868px;width:920px;text-align:center;font-size:17px;line-height:34.5px;color:#2a2a2a}
.green-band{left:0;top:1465px;width:1200px;height:936px;background:linear-gradient(180deg,#3f6a36 0%,#44703a 60%,#3a6430 100%)}
.video{left:140px;top:1090px;width:918px;height:484px;background:linear-gradient(135deg,#3a2a22 0%,#a4462c 35%,#d9a27a 60%,#5c7a45 100%);box-shadow:0 6px 18px rgba(0,0,0,.25)}
.play{left:564px;top:1303px;width:70px;height:58px;border-radius:50%;background:rgba(255,255,255,.9)}

/* services */
.services-title{top:1646px;color:var(--white)}
.card{background:var(--white);border-radius:6px;overflow:hidden}
.card .photo{width:100%;height:313px}
.card h3{text-align:center;font-size:30px;color:var(--ink);margin-top:30px}
.card p{text-align:center;font-size:17px;line-height:32.5px;color:#444;padding:0 30px;margin-top:6px}
.card .more{text-align:center;font-size:15px;font-weight:500;color:var(--green);text-decoration:underline;margin-top:12px}

/* values */
.value-ring{left:393px;top:2564px;width:410px;height:410px;border-radius:50%;border:1px solid #ddd}
.value-logo{left:398px;top:2700px;width:400px;text-align:center;color:var(--green);line-height:1}
.value-logo span{display:block;font-size:62px}
.icon{width:64px;height:64px;border-radius:50%;background:var(--green);display:flex;align-items:center;justify-content:center}
.vlabel{font-size:16px;font-weight:500;line-height:23px;color:#222}
.vlabel.r{text-align:right}

/* about */
.about-photo{left:0;top:2964px;width:602px;height:471px;background:linear-gradient(120deg,#c8cdd0 0%,#b83a30 40%,#d2a17f 55%,#4f7a3a 75%,#d6d8d8 100%)}
.about-panel{left:602px;top:2964px;width:598px;height:471px;background:var(--green)}
.about-panel h2{position:absolute;left:38px;top:58px;color:var(--white);font-size:40px}
.about-panel p{position:absolute;left:34px;top:125px;width:520px;color:var(--white);font-size:15.5px;line-height:32.5px}
.about-panel .btn{position:absolute;left:38px;top:344px;width:190px;height:48px;border:2px solid var(--white);border-radius:24px;color:var(--white);font-weight:700;font-size:15px;display:flex;align-items:center;justify-content:center;gap:6px}

/* news */
.news{background:var(--white);box-shadow:0 2px 10px rgba(0,0,0,.12);width:310px;height:384px}
.news .photo{height:193px}
.news h4{font-size:19px;line-height:26px;color:#111;padding:22px 14px 0;font-weight:500}
.news p{font-size:12px;line-height:23px;color:#555;padding:4px 14px 0}
.news .more{font-size:13px;font-weight:700;color:var(--green);text-decoration:underline;padding:14px 14px 0}

/* footer */
.footer{left:0;top:4061px;width:1200px;height:341px;background:var(--footer);color:var(--white)}
.footer .brand{left:110px;top:62px;color:var(--white)}
.footer .contact{position:absolute;left:113px;top:170px;font-size:14px;line-height:25px}
.footer h5{position:absolute;font-size:16px;font-weight:500;top:63px;letter-spacing:.3px}
.footer ul{position:absolute;top:101px;list-style:none;font-size:13.5px;line-height:26px}
.social{position:absolute;left:926px;top:100px;display:flex;gap:9px}
.social i{width:32px;height:32px;border-radius:50%;background:#666}
.footer .rule{position:absolute;left:113px;top:265px;width:976px;height:1px;background:#333}
.footer .copy{position:absolute;left:113px;top:300px;font-size:13.5px}
.footer .legal{position:absolute;right:111px;top:300px;font-size:13.5px;display:flex;gap:28px}
</style>
</head>
<body>

<header>
  <div class="abs brand serif"><span class="l1">Velbrook</span><span class="l2">Trade AG</span></div>
  <div class="abs search">Search<span class="btn">
    <svg width="28" height="28" viewBox="0 0 28 28"><circle cx="13" cy="13" r="5" fill="none" stroke="#fff" stroke-width="2"/><line x1="17" y1="17" x2="20" y2="20" stroke="#fff" stroke-width="2"/></svg></span></div>
  <div class="abs lang" aria-label="Language selector"></div>
  <div class="abs caret"></div>
  <nav class="abs nav"><ul>
    <li>HOME</li><li class="sep">|</li><li>ABOUT US</li><li class="sep">|</li><li>PRODUCTS</li><li class="sep">|</li><li>SERVICES</li><li class="sep">|</li><li>CONTACT</li>
  </ul></nav>
</header>

<section class="abs hero" role="img" aria-label="Warehouse with stacked sacks of ingredients and a forklift">
  <h1 class="abs serif">Velbrook Trade AG</h1>
  <p class="abs">Sed ut perspiciatis unde omnis iste natus error sit voluptatem accusantium</p>
  <div class="abs cta">GET STARTED
    <svg width="14" height="14" viewBox="0 0 14 14"><circle cx="7" cy="7" r="7" fill="#fff"/><path d="M5.5 4l3 3-3 3" stroke="#3b6533" stroke-width="2" fill="none"/></svg></div>
  <svg class="abs" style="left:62px;top:285px" width="26" height="50" viewBox="0 0 26 50"><path d="M22 4L4 25l18 21" stroke="#fff" stroke-width="2.5" fill="none"/></svg>
  <svg class="abs" style="left:1104px;top:285px" width="26" height="50" viewBox="0 0 26 50"><path d="M4 4l18 21L4 46" stroke="#fff" stroke-width="2.5" fill="none"/></svg>
  <div class="abs dots"><i class="on"></i><i></i></div>
</section>

<h2 class="abs section-title serif" style="top:790px">Welcome To Velbrook Trade AG</h2>
<p class="abs welcome-text">Sed ut perspiciatis unde omnis iste natus error sit voluptatem accusantium doloremque laudantium, totam rem aperiam, eaque ipsa quae ab illo inventore veritatis et quasi architecto beatae vitae dicta sunt explicabo. Nemo enim ipsam voluptatem quia voluptas sit aspernatur aut odit aut fugit, sed quia consequuntur magni dolores eos qui ratione voluptatem sequi nesciunt. Neque porro quisquam est, qui dolorem ipsum quia dolor sit amet, consectetur, adipisci velit, sed quia non numquam eius modi tempora incidunt ut labore et dolore magnam</p>

<div class="abs green-band" role="img" aria-label="Green crop field in soft focus"></div>
<div class="abs video" role="img" aria-label="Video still: worker sorting crates of fresh peaches"></div>
<div class="abs play"><svg width="70" height="58" viewBox="0 0 70 58"><path d="M29 19l15 10-15 10z" fill="#3b6533"/></svg></div>

<h2 class="abs section-title serif services-title">Our Services</h2>
<article class="abs card" style="left:111px;top:1741px;width:470px;height:537px">
  <div class="photo" role="img" aria-label="Market worker holding a parcel of organic produce" style="background:linear-gradient(135deg,#8c9a8a,#5d6b4e 50%,#b8a07a)"></div>
  <h3 class="serif">Trading</h3>
  <p>Lorem ipsum dolor sit amet, consectetur adipiscing elit, sed do eiusmod tempor incididunt ut labore et dolore magna aliqua.</p>
  <div class="more">LEARN MORE ➜</div>
</article>
<article class="abs card" style="left:619px;top:1741px;width:470px;height:537px">
  <div class="photo" role="img" aria-label="Worker unloading pallets from a truck" style="background:linear-gradient(135deg,#3a3a3a,#6b6f72 45%,#a8653a 70%,#8a8478)"></div>
  <h3 class="serif">Marketing</h3>
  <p>Lorem ipsum dolor sit amet, consectetur adipiscing elit, sed do eiusmod tempor incididunt ut labore et dolore magna aliqua.</p>
  <div class="more">LEARN MORE ➜</div>
</article>

<h2 class="abs section-title serif" style="top:2476px">Our Values</h2>
<div class="abs value-ring"></div>
<div class="abs value-logo serif"><span>Velbrook</span><span>Trade AG</span></div>

<div class="abs vlabel r" style="left:200px;top:2609px;width:240px">Health &amp; Nutritional<br>Health</div>
<div class="abs icon" style="left:452px;top:2600px"><svg width="34" height="34" viewBox="0 0 34 34" fill="none" stroke="#fff" stroke-width="2"><rect x="8" y="5" width="18" height="24" rx="2"/><path d="M12 12h10M12 17h10M12 22h6"/></svg></div>
<div class="abs vlabel r" style="left:120px;top:2701px;width:242px">Eco-friendly and<br>Sustainability</div>
<div class="abs icon" style="left:373px;top:2691px"><svg width="34" height="34" viewBox="0 0 34 34" fill="none" stroke="#fff" stroke-width="2"><circle cx="17" cy="17" r="11"/><path d="M12 20c4-1 8-5 9-10"/></svg></div>
<div class="abs vlabel r" style="left:80px;top:2811px;width:282px">High Quality Standard in term of<br>products and logistic services</div>
<div class="abs icon" style="left:373px;top:2802px"><svg width="34" height="34" viewBox="0 0 34 34" fill="none" stroke="#fff" stroke-width="2"><rect x="7" y="9" width="20" height="18"/><path d="M7 15h20M17 9v18"/></svg></div>

<div class="abs icon" style="left:682px;top:2600px"><svg width="34" height="34" viewBox="0 0 34 34" fill="none" stroke="#fff" stroke-width="2"><circle cx="17" cy="17" r="11"/><path d="M12 17l4 4 7-8"/></svg></div>
<div class="abs vlabel" style="left:757px;top:2611px;width:240px">Trust and reliability</div>
<div class="abs icon" style="left:758px;top:2691px"><svg width="34" height="34" viewBox="0 0 34 34" fill="none" stroke="#fff" stroke-width="2"><circle cx="17" cy="17" r="5"/><path d="M17 5v5M17 24v5M5 17h5M24 17h5"/></svg></div>
<div class="abs vlabel" style="left:836px;top:2701px;width:240px">Flexibility &amp; speed to<br>market</div>
<div class="abs icon" style="left:758px;top:2802px"><svg width="34" height="34" viewBox="0 0 34 34" fill="none" stroke="#fff" stroke-width="2"><rect x="7" y="7" width="20" height="20" rx="2"/><path d="M11 13h12M11 18h12M11 23h7"/></svg></div>
<div class="abs vlabel" style="left:836px;top:2807px;width:300px">Technical advice for the development of new products (Functional Food &amp; Food Supplements),</div>

<div class="abs about-photo" role="img" aria-label="Smiling grocer holding a crate of fresh vegetables"></div>
<section class="abs about-panel">
  <h2 class="serif">About Us</h2>
  <p>Sed ut perspiciatis unde omnis iste natus erroptatem accusantium doloremque laudantium, totam rem a quae ab illo inventore veritatis et quasi architectoae vitae dicta sunt explicabo. Nemo enim ipsam voluptatem quia voluptas sit aspernatur aut odit aut fugit, sed quia consequntur magni es eos qui ratione voluptatem sequi nesciunt. Neque porro quisquam est, qui</p>
  <div class="btn">LEARN MORE
    <svg width="14" height="14" viewBox="0 0 14 14"><circle cx="7" cy="7" r="7" fill="#fff"/><path d="M5.5 4l3 3-3 3" stroke="#3b6533" stroke-width="2" fill="none"/></svg></div>
</section>

<h2 class="abs section-title serif" style="top:3506px">Latest News</h2>
<article class="abs news" style="left:113px;top:3591px">
  <div class="photo" role="img" aria-label="Warehouse with crates of melons" style="background:linear-gradient(135deg,#4c5a3a,#7b8f4a 50%,#3a3a36)"></div>
  <h4>The standard Lorem Ipsum passage, used since</h4>
  <p>Sed ut peatus error sit voluptatem accusantium doremque laudantium, totamm aperiam, eaque ipsa quae ab illo inventore</p>
  <div class="more">READ MORE...</div>
</article>
<article class="abs news" style="left:445px;top:3591px">
  <div class="photo" role="img" aria-label="Workers sorting tomatoes on a packing line" style="background:linear-gradient(135deg,#6c8f3a,#c8453a 50%,#e07a3a)"></div>
  <h4>The standard Lorem Ipsum passage, used since</h4>
  <p>Sed ut peatus error sit voluptatem accusantium doremque laudantium, totamm aperiam, eaque ipsa quae ab illo inventore</p>
  <div class="more">READ MORE...</div>
</article>
<article class="abs news" style="left:778px;top:3591px">
  <div class="photo" role="img" aria-label="Warehouse worker scanning boxes" style="background:linear-gradient(135deg,#7a5a3e,#b08a64 50%,#d8d4cc)"></div>
  <h4>The standard Lorem Ipsum passage, used since</h4>
  <p>Sed ut peatus error sit voluptatem accusantium doremque laudantium, totamm aperiam, eaque ipsa quae ab illo inventore</p>
  <div class="more">READ MORE...</div>
</article>

<footer class="abs footer">
  <div class="abs brand serif"><span class="l1">Velbrook</span><span class="l2">Trade AG</span></div>
  <div class="contact">info@velbrooktrade.com<br>Mobile: +1 555 0100 0100<br>1234 Fieldway Lane Anytown 21212</div>
  <h5 style="left:445px">QUICK LINKS</h5>
  <ul style="left:445px"><li>Home</li><li>About Us</li><li>Products</li><li>Services</li><li>Contact</li></ul>
  <h5 style="left:664px">USEFUL LINKS</h5>
  <ul style="left:664px"><li>Awards &amp; Accreditations</li><li>Health &amp; Safety</li><li>Insurances</li><li>Privacy Policy</li><li>Sitemap</li></ul>
  <h5 style="left:933px">STAY CONNECTED</h5>
  <div class="social"><i></i><i></i><i></i><i></i></div>
  <div class="rule"></div>
  <div class="copy">Copyright © 2022 VELBROOK TRADE AG . All Rights Reserved.</div>
  <div class="legal"><span>Terms &amp; Conditions</span><span>Privacy Policy</span><span>About Us</span><span>Support</span></div>
</footer>

</body>
</html>
```